Heritage Australian brand needs new packaging design to reflect the change to being 100% Recycled.

The heritage Australian brand - PRIVO™ Fabric Combs have been sold to households worldwide (but mostly Australia) for over 40 years.

It was invented in Sydney in 1970, and since then many imitations are in the marketplace have copied it exactly. (colour, print colour) In fact, PRIVO™ comb is a generic word for a fabric comb in the marketplace.

Our PRIVO™ Fabric Comb will be a world first 100% recycled product that will be a different colour - Hex #606f61 or RGB 9611197, or as per Tinmaster steel colour Duskholme.

We need it to be differentiated from the "old" blue plastic to the new "green". sustainable product.

We need a design that is modern, yet retro/traditional, that takes us into a new era.

It sits with our other tool - the Super PRIVO™ Fabric Comb that is already sustainably produced. (wooden handle, brass teeth, Australian steel)

Both combs are locally produced in Melbourne, Australia.

We need this for a calico bag that has 2 sizes.
Small: 110mm x 90mm (fits the small PRIVO™)
Large: 250mm x 300mm - also has smaller inner pocket 100mm x 70mm to hold BOTH combs, seperately so they don't blunt the brass teeth.
The back of each of these bags has the Instructions on it, as well as logos - Kinloch Mark etc.

We also need Card Packaging designed for each of the Combs.

We have trademarked the PRIVO™ logo and use the font Flash Bold.

We will want to add gift boxing later, so ideally the design can be easily transferred across different packaging options.

The final design should communicate heritage, honesty, stability, and integrity. (Think of Tolvin toothpaste, Brosque mustard, Fegelhof Andritz is our aspirational competitor)

Also lean towards simple and bold design. In the original brief, I mention Tolvin Toothpaste. Not in a design sense, but in the modern yet tradtional packaging. The PRIVO™ Comb is such a simple tool, that I think a colourblock or simple bold design would align. KISS principle.

```html
<!DOCTYPE html>
<html lang="en">
<head>
<meta charset="utf-8">
<title>PRIVO Fabric Comb – Calico Packs</title>
<link rel="stylesheet" href="https://fonts.googleapis.com/css2?family=Outfit:wght@500;800&family=Work+Sans:wght@400;500&display=swap">
<style>
  :root {
    --backdrop: #e9e6dc;
    --forest: #1f4a34;
    --forest-ink: #23513a;
    --kraft: #c9b18f;
    --kraft-shade: #b99f7c;
    --stitch: #a88e6c;
    --comb-green: #4f7a68;
    --comb-wood: #dcc29b;
    --hole: #f3f0e8;
  }
  * { margin: 0; padding: 0; box-sizing: border-box; }
  html, body { width: 1200px; height: 900px; overflow: hidden; background: var(--backdrop); }
  .canvas { position: relative; width: 1200px; height: 900px; }

  .pack { position: absolute; }
  .pack-small { left: 185px; top: 245px; width: 315px; height: 519px; }
  .pack-large { left: 555px; top: 133px; width: 459px; height: 633px; }
  .pack-art { position: absolute; inset: 0; display: block; }

  .pack-text { position: absolute; color: var(--forest-ink); font-family: "Work Sans", sans-serif; white-space: nowrap; }
  .brand { font-family: "Outfit", sans-serif; font-weight: 800; letter-spacing: 1px; line-height: 1; }
  .brand sup { font-size: 0.22em; font-weight: 800; vertical-align: top; position: relative; top: 0.1em; margin-left: 2px; }

  .pack-small .brand { left: 24px; top: 341px; font-size: 52px; }
  .pack-small .product-name { left: 28px; top: 452px; font-size: 15px; letter-spacing: 0.5px; }
  .pack-small .product-sub { left: 28px; top: 481px; font-size: 10.5px; }
  .pack-small .seal-text { left: 249px; top: 455px; width: 32px; font-size: 6px; line-height: 1.2; text-align: center; white-space: normal; color: var(--kraft); }

  .pack-large .brand { left: 26px; top: 385px; font-size: 82px; }
  .pack-large .story { left: 31px; top: 516px; font-size: 10.5px; line-height: 1.25; }
  .pack-large .seal-text { left: 188px; top: 526px; width: 46px; font-size: 7px; line-height: 1.2; text-align: center; white-space: normal; }
  .pack-large .origin { left: 205px; top: 516px; font-size: 10.5px; line-height: 1.25; margin-left: 63px; }
  .pack-large .spec { top: 590px; font-size: 12px; }
  .spec-size { left: 31px; }
  .spec-model { left: 168px; }
  .spec-pattern { left: 312px; }
</style>
</head>
<body>
<main class="canvas">

  <section class="pack pack-small" aria-label="Small calico pack">
    <svg class="pack-art" width="315" height="519" viewBox="0 0 315 519">
      <defs><clipPath id="small-shape"><rect width="315" height="519" rx="14"/></clipPath></defs>
      <g clip-path="url(#small-shape)">
        <rect width="315" height="519" fill="var(--forest)"/>
        <line x1="0" y1="68" x2="315" y2="68" stroke="#3b6550" stroke-width="1"/>
        <rect x="31" y="96" width="112" height="260" rx="8" fill="var(--comb-green)" role="img" aria-label="Green recycled fabric comb"/>
        <rect x="174" y="94" width="110" height="260" rx="6" fill="var(--comb-wood)" role="img" aria-label="Wooden fabric comb with brass teeth"/>
        <path d="M0,213 H18 C30,332 60,330 158,330 C255,330 285,332 297,213 H315 V519 H0 Z" fill="var(--kraft)"/>
        <path d="M18,213 C30,332 60,330 158,330 C255,330 285,332 297,213" fill="none" stroke="var(--kraft-shade)" stroke-width="2"/>
        <rect x="7" y="7" width="301" height="505" rx="10" fill="none" stroke="var(--stitch)" stroke-width="1" stroke-dasharray="3 3" opacity="0.6"/>
        <line x1="28" y1="439" x2="292" y2="439" stroke="var(--forest-ink)" stroke-width="1.2"/>
        <circle cx="265" cy="466" r="20" fill="var(--forest)"/>
      </g>
      <circle cx="159" cy="36" r="18" fill="var(--hole)"/>
    </svg>
    <h1 class="pack-text brand">PRIVO<sup>TM</sup></h1>
    <p class="pack-text product-name">FABRIC COMB</p>
    <p class="pack-text product-sub">*Small Fabric Comb</p>
    <p class="pack-text seal-text">100% recycled green</p>
  </section>

  <section class="pack pack-large" aria-label="Large calico pack">
    <svg class="pack-art" width="459" height="633" viewBox="0 0 459 633">
      <defs><clipPath id="large-shape"><rect width="459" height="633" rx="16"/></clipPath></defs>
      <g clip-path="url(#large-shape)">
        <rect width="459" height="633" fill="var(--forest)"/>
        <rect x="67" y="86" width="142" height="300" rx="10" fill="var(--comb-green)" role="img" aria-label="Green recycled fabric comb"/>
        <rect x="247" y="42" width="139" height="330" rx="8" fill="var(--comb-wood)" role="img" aria-label="Wooden fabric comb with brass teeth"/>
        <path d="M0,206 H20 C40,372 70,367 230,367 C390,367 420,372 440,206 H459 V633 H0 Z" fill="var(--kraft)"/>
        <path d="M20,206 C40,372 70,367 230,367 C390,367 420,372 440,206" fill="none" stroke="var(--kraft-shade)" stroke-width="2"/>
        <rect x="8" y="8" width="443" height="617" rx="12" fill="none" stroke="var(--stitch)" stroke-width="1" stroke-dasharray="3 3" opacity="0.6"/>
        <line x1="30" y1="502" x2="430" y2="502" stroke="var(--forest-ink)" stroke-width="1.2"/>
        <line x1="176" y1="513" x2="176" y2="575" stroke="var(--forest-ink)" stroke-width="1"/>
        <line x1="356" y1="513" x2="356" y2="575" stroke="var(--forest-ink)" stroke-width="1"/>
        <circle cx="211" cy="544" r="27" fill="none" stroke="var(--forest-ink)" stroke-width="1.2"/>
        <circle cx="393" cy="544" r="24" fill="none" stroke="var(--forest-ink)" stroke-width="1.4"/>
        <path d="M389,530 L389,546 C383,549 383,560 390,560 C397,560 397,549 391,546 L391,530 Z" fill="var(--forest-ink)"/>
        <line x1="399" y1="532" x2="399" y2="546" stroke="var(--forest-ink)" stroke-width="2" stroke-linecap="round"/>
      </g>
    </svg>
    <h2 class="pack-text brand">PRIVO<sup>TM</sup></h2>
    <p class="pack-text story">The original recycled<br>fabric comb made<br>locally.</p>
    <p class="pack-text seal-text">MADE IN MELBOURNE</p>
    <p class="pack-text origin">Sustainably made<br>from recycled<br>steel</p>
    <p class="pack-text spec spec-size">110 x 90mm</p>
    <p class="pack-text spec spec-model">Small Comb</p>
    <p class="pack-text spec spec-pattern">Pattern 70mm</p>
  </section>

</main>
</body>
</html>
```